Resume for CEO

I need two formats of a resume created.

#1. It is 3 pages long and is the extended version.

#2. Is the 1 page resume.

Both should have the same styling. I am attaching the long and short version in word. I am also attaching a temporary picture for the resume. I will switch that out myself. Don't worry about keeping the sizing. It can be whatever you want.

There is a good website to use as a reference. http://quillpagecraft.com/
The reason I am not using this site is because they don't give you the files for editing. They make you use them to edit.

Please feel free to ask questions. I"m excited to see the ideas that come up.

End format should be in AI with PDF's. I want 1 resume that is 3-4 pages and one that is 1 page. They should have the same style.

Dale

Reason: I have only received 2 designs. Hopefully I can get more submissions.

Reason: I need to get the design finalized and I will end the project.

```html
<!DOCTYPE html>
<html lang="en">
<head>
<meta charset="utf-8">
<title>Dale S. Hartwell – Resume</title>
<link rel="stylesheet" href="https://fonts.googleapis.com/css2?family=Arimo:wght@400;700&family=Libre+Baskerville:wght@700&display=swap">
<style>
  :root {
    --canvas: #ffffff;
    --panel: #eeeff2;
    --band-light: #e4e5e8;
    --band-dark: #c9cbd0;
    --text: #1a1a1a;
    --white: #ffffff;
    --navy: #1f2a3b;
    --maroon: #650e0a;
  }
  * { box-sizing: border-box; margin: 0; padding: 0; }
  html, body { width: 1200px; height: 766px; overflow: hidden; background: var(--canvas); }
  body { position: relative; font-family: "Arimo", Arial, sans-serif; color: var(--text); }

  .resume {
    position: absolute; top: 27px; width: 549px; height: 712px;
    background: var(--canvas); border: 1px solid #d6d6d6;
  }
  .resume--navy { left: 30px; --accent: var(--navy); }
  .resume--maroon { left: 620px; --accent: var(--maroon); }

  .resume__topbar { position: absolute; left: 0; top: 0; width: 100%; height: 15px; background: var(--accent); }

  .resume__name {
    position: absolute; left: 0; top: 26px; width: 100%; text-align: center;
    font-family: "Libre Baskerville", Georgia, serif; font-weight: 700;
    font-size: 37px; letter-spacing: 0.5px; color: var(--accent);
    text-shadow: 2px 2px 2px rgba(0,0,0,0.35);
  }
  .resume__title {
    position: absolute; left: 0; top: 75px; width: 100%; text-align: center;
    font-weight: 700; font-size: 15px; letter-spacing: 0.2px; color: var(--text);
  }
  .resume__title .dots { color: var(--accent); letter-spacing: 3px; margin: 0 14px; font-size: 13px; }

  .section-head {
    position: absolute; height: 21px; display: flex; align-items: flex-start;
    background: linear-gradient(to right, var(--band-dark), var(--band-light) 40%, var(--band-light));
    border-bottom: 2px solid var(--accent);
    font-family: "Libre Baskerville", Georgia, serif; font-weight: 700;
    font-size: 9px; text-transform: uppercase; letter-spacing: 0.3px;
  }
  .section-head__tab {
    flex: none; height: 19px; padding: 5px 18px 0 11px;
    background: var(--accent); color: var(--white);
    clip-path: polygon(0 0, 100% 0, calc(100% - 10px) 100%, 0 100%);
  }
  .section-head__rest { flex: none; margin-left: 1px; padding-top: 5px; color: var(--accent); white-space: nowrap; }

  .panel { position: absolute; background: var(--panel); }

  .profile__text {
    position: absolute; left: 47px; top: 143px; width: 288px;
    font-size: 9.6px; line-height: 11.9px; color: var(--text);
  }
  .profile__photo {
    position: absolute; left: 367px; top: 139px; width: 111px; height: 146px;
    background: linear-gradient(160deg, #b39b6c 0%, #6b5236 45%, #3a3a3c 75%, #2b2c30 100%);
    box-shadow: 4px 4px 3px rgba(0,0,0,0.45);
  }

  .achievements {
    position: absolute; left: 43px; top: 333px; width: 215px;
    list-style: none; font-size: 9.4px; line-height: 11.2px;
  }
  .achievements li { position: relative; padding-left: 11px; margin-bottom: 5px; }
  .achievements li::before { content: "•"; position: absolute; left: 0; top: 0; }

  .tag-list {
    position: absolute; left: 294px; width: 230px; list-style: none;
    font-weight: 700; font-size: 8.6px; line-height: 13.45px; text-transform: uppercase;
    white-space: nowrap;
  }
  .tag-list li::before { content: "•"; margin-right: 5px; }
  .tag-list--core { top: 329px; }
  .tag-list--industry { top: 515px; }

  .resume__footer {
    position: absolute; left: 0; bottom: 0; width: 100%; height: 49px;
    background: var(--accent); color: var(--white); text-align: center;
    font-weight: 700; font-size: 10.6px; line-height: 16px; padding-top: 9px;
  }
</style>
</head>
<body>

  <article class="resume resume--navy">
    <div class="resume__topbar"></div>
    <h1 class="resume__name">DALE S. HARTWELL</h1>
    <p class="resume__title"><span class="dots">▪▪▪▪</span>CHIEF EXECUTIVE OFFICER &nbsp;/&nbsp; ENTREPRENEUR<span class="dots">▪▪▪▪</span></p>

    <div class="section-head" style="left:30px; top:104px; width:489px;"><span class="section-head__tab">Profile</span></div>
    <div class="panel" style="left:30px; top:125px; width:489px; height:166px;"></div>
    <p class="profile__text">Dynamic Chief Executive Officer with over 16 years of experience in providing strategic direction and leadership for organizations in multiple markets with unique situations. &nbsp; Extensive experience transforming companies into profitable and progressive organiza&shy;tions using proven systematic implementation. Offers comprehen&shy;sive knowledge and operational experience with highly-engineered technical manufacturing companies, ecommerce and international brand building. Effectively identifies critical business drivers in multiple markets and industries, enabling growth oppor&shy;tunities within a variety of departments and ultimately complete business expansion.</p>
    <div class="profile__photo" role="img" aria-label="Portrait photo of the candidate in a dark blazer"></div>

    <div class="section-head" style="left:30px; top:302px; width:237px;"><span class="section-head__tab">Career</span><span class="section-head__rest">Achievements</span></div>
    <div class="panel" style="left:30px; top:323px; width:237px; height:317px;"></div>
    <ul class="achievements">
      <li>Constructed multiple start-up companies from ground-up utilizing organic growth strategies with little capital demonstrating consistent expansions and sales increase, accelerating into well-known international brands.</li>
      <li>Corporate restructuring and turnaround deploy&shy;ment, assisting several companies from decline and near insolvency into profitable states by streamlining the organization and renovating management, marketing, and sales strategies.</li>
      <li>Produced measurable year-after-year improve&shy;ment under shifting conditions and economically depressed markets by adopting “lean mentality” and “just-in-time” strategies.</li>
      <li>Conceived and led revenue capture strategies, successfully achieving positive sales trajectories in addition to designing and sourcing innovative and industry-altering technologies.</li>
      <li>Rebuilt and rejuvenated leadership staff into unified, top-performing, and highly motivated teams. Utilizing these teams to secure strong international distribution by expanding busi&shy;nesses into international markets.</li>
    </ul>

    <div class="section-head" style="left:285px; top:302px; width:233px;"><span class="section-head__tab">Core</span><span class="section-head__rest">Competencies</span></div>
    <div class="panel" style="left:285px; top:323px; width:233px; height:317px;"></div>
    <ul class="tag-list tag-list--core">
      <li>Chief Executive Officer</li><li>Turnaround</li><li>Organic Business Growth</li><li>Brand Building</li><li>Business Development</li><li>Contract Manufacturing</li><li>Strong Financial Accounting</li><li>Corporate Restructuring</li><li>Strategic Sales Planning</li><li>Key Management Construction</li><li>Marketing Strategies</li>
    </ul>
    <div class="section-head" style="left:285px; top:487px; width:233px;"><span class="section-head__tab">Industry</span><span class="section-head__rest">Specializations</span></div>
    <ul class="tag-list tag-list--industry">
      <li>International Business</li><li>Outdoor Sporting Goods &amp; Action Sports</li><li>Ecommerce &amp; Specialty Retail</li><li>Int. Distribution &amp; Logistics</li><li>Sales &amp; Marketing Strategies</li><li>Acquisitions &amp; Integrations</li><li>Corporate Funding</li><li>Corporate Restructuring</li>
    </ul>

    <footer class="resume__footer">4870 Harbor View Rd. Ste. 210 - San Diego, CA 92130<br>(619) 555-0142 - dalehartwell22@mailbox.com</footer>
  </article>

  <article class="resume resume--maroon">
    <div class="resume__topbar"></div>
    <h1 class="resume__name">DALE S. HARTWELL</h1>
    <p class="resume__title"><span class="dots">▪▪▪▪</span>CHIEF EXECUTIVE OFFICER &nbsp;/&nbsp; ENTREPRENEUR<span class="dots">▪▪▪▪</span></p>

    <div class="section-head" style="left:30px; top:104px; width:489px;"><span class="section-head__tab">Profile</span></div>
    <div class="panel" style="left:30px; top:125px; width:489px; height:166px;"></div>
    <p class="profile__text">Dynamic Chief Executive Officer with over 16 years of experience in providing strategic direction and leadership for organizations in multiple markets with unique situations. &nbsp; Extensive experience transforming companies into profitable and progressive organiza&shy;tions using proven systematic implementation. Offers comprehen&shy;sive knowledge and operational experience with highly-engineered technical manufacturing companies, ecommerce and international brand building. Effectively identifies critical business drivers in multiple markets and industries, enabling growth oppor&shy;tunities within a variety of departments and ultimately complete business expansion.</p>
    <div class="profile__photo" role="img" aria-label="Portrait photo of the candidate in a dark blazer"></div>

    <div class="section-head" style="left:30px; top:302px; width:237px;"><span class="section-head__tab">Career</span><span class="section-head__rest">Achievements</span></div>
    <div class="panel" style="left:30px; top:323px; width:237px; height:317px;"></div>
    <ul class="achievements">
      <li>Constructed multiple start-up companies from ground-up utilizing organic growth strategies with little capital demonstrating consistent expansions and sales increase, accelerating into well-known international brands.</li>
      <li>Corporate restructuring and turnaround deploy&shy;ment, assisting several companies from decline and near insolvency into profitable states by streamlining the organization and renovating management, marketing, and sales strategies.</li>
      <li>Produced measurable year-after-year improve&shy;ment under shifting conditions and economically depressed markets by adopting “lean mentality” and “just-in-time” strategies.</li>
      <li>Conceived and led revenue capture strategies, successfully achieving positive sales trajectories in addition to designing and sourcing innovative and industry-altering technologies.</li>
      <li>Rebuilt and rejuvenated leadership staff into unified, top-performing, and highly motivated teams. Utilizing these teams to secure strong international distribution by expanding busi&shy;nesses into international markets.</li>
    </ul>

    <div class="section-head" style="left:285px; top:302px; width:233px;"><span class="section-head__tab">Core</span><span class="section-head__rest">Competencies</span></div>
    <div class="panel" style="left:285px; top:323px; width:233px; height:317px;"></div>
    <ul class="tag-list tag-list--core">
      <li>Chief Executive Officer</li><li>Turnaround</li><li>Organic Business Growth</li><li>Brand Building</li><li>Business Development</li><li>Contract Manufacturing</li><li>Strong Financial Accounting</li><li>Corporate Restructuring</li><li>Strategic Sales Planning</li><li>Key Management Construction</li><li>Marketing Strategies</li>
    </ul>
    <div class="section-head" style="left:285px; top:487px; width:233px;"><span class="section-head__tab">Industry</span><span class="section-head__rest">Specializations</span></div>
    <ul class="tag-list tag-list--industry">
      <li>International Business</li><li>Outdoor Sporting Goods &amp; Action Sports</li><li>Ecommerce &amp; Specialty Retail</li><li>Int. Distribution &amp; Logistics</li><li>Sales &amp; Marketing Strategies</li><li>Acquisitions &amp; Integrations</li><li>Corporate Funding</li><li>Corporate Restructuring</li>
    </ul>

    <footer class="resume__footer">4870 Harbor View Rd. Ste. 210 - San Diego, CA 92130<br>(619) 555-0142 - dalehartwell22@mailbox.com</footer>
  </article>

</body>
</html>
```